Web Design Project

I need a webpage design for the following:
The website is a Niche Community for Specialists (engineers) in the Energy sector. We have a pool of elite engineers
It should be simple. We need the following:
* Home. go to ridgeloom.com That's the content (plus the credits at the bottom of the page). Very simple. We only need design now!
* Thank you page. The logo at the top and "Thank you for sending your information....etc" that's it
* Register... list of questions to register
* Personal page (where the user will manage their profile)
the logo is the one in www.ridgeloom.com
Look and feel
Each slider illustrates characteristics of the customer's brand and the style your logo design should communicate.

```html
<!DOCTYPE html>
<html lang="en">
<head>
<meta charset="utf-8">
<title>Ridgeloom — Community Site for Engineers</title>
<link rel="stylesheet" href="https://fonts.googleapis.com/css2?family=Arimo:wght@400;700&family=Noto+Sans:wght@400&display=swap">
<style>
  :root {
    --navy: #143459;
    --ink: #222222;
    --muted: #555555;
    --bar-top: #4a4a4a;
    --bar-bottom: #1e1e1e;
    --login-top: #3aa2dc;
    --login-bottom: #1670ae;
    --peach: #f6dfc8;
    --peach-light: #fbeee2;
    --peach-edge: #f2e3d6;
    --footer-bg: #efebe6;
    --footer-line: #cfc9c2;
    --social: #7a7672;
    --white: #ffffff;
  }
  * { box-sizing: border-box; margin: 0; padding: 0; }
  html, body { width: 1200px; height: 1188px; overflow: hidden; }
  body {
    position: relative;
    background: var(--white);
    font-family: "Arimo", Arial, sans-serif;
    color: var(--ink);
  }
  .abs { position: absolute; }

  /* Top bar */
  .top-bar {
    left: 0; top: 0; width: 1200px; height: 47px;
    background: linear-gradient(var(--bar-top), var(--bar-bottom));
    border-bottom: 1px solid #111;
  }
  .login-field {
    top: 11px; height: 26px; width: 147px;
    background: var(--white); border-radius: 9px;
    font-size: 13px; color: #333; padding: 5px 0 0 16px;
    box-shadow: inset 0 1px 2px rgba(0,0,0,.3);
  }
  .login-field.username { left: 681px; }
  .login-field.password { left: 840px; }
  .login-button {
    left: 996px; top: 10px; width: 81px; height: 28px;
    border-radius: 7px;
    background: linear-gradient(var(--login-top), var(--login-bottom));
    color: var(--white); font-size: 13px; text-align: center; line-height: 28px;
  }

  /* Header */
  .brand {
    left: 54px; top: 76px;
    font-size: 64px; font-weight: 700; color: var(--navy);
    letter-spacing: -2px; line-height: 80px;
  }
  .about-button {
    left: 874px; top: 88px; width: 195px; height: 66px;
    border-radius: 8px; border: 1px solid #c9d3dc;
    background: linear-gradient(#ffffff, #dde5ec);
    box-shadow: 0 6px 10px rgba(0,0,0,.12);
  }
  .about-button .label {
    position: absolute; left: 15px; top: 16px;
    font-size: 27px; font-weight: 700; color: var(--navy); letter-spacing: -1px;
  }
  .about-button .icon {
    position: absolute; left: 148px; top: 14px; width: 38px; height: 38px;
    border-radius: 50%;
    background: linear-gradient(135deg, #8fbf6a, #7fb0d8 55%, #e98a3c);
  }

  /* Hero */
  .hero-band {
    left: 0; top: 199px; width: 1200px; height: 406px;
    background: linear-gradient(90deg, var(--peach-edge), var(--peach-light) 50%, var(--peach-edge));
  }
  .nav-band {
    left: 0; top: 199px; width: 1200px; height: 60px;
    background: linear-gradient(90deg, #f4d9bf, var(--peach) 50%, #f4d9bf);
  }
  .hero-panel {
    left: 54px; top: 199px; width: 1090px; height: 406px;
    background: linear-gradient(#fbeadb, #fdf3ea 45%, #fbe9d9);
    box-shadow: 0 4px 18px rgba(0,0,0,.28);
  }
  .main-nav {
    position: absolute; left: 0; top: 0; width: 1090px; height: 60px;
    background: linear-gradient(#f9e1c9, #f5d8bb);
    border-bottom: 1px solid #ecd0b3;
    list-style: none;
  }
  .main-nav li {
    position: absolute; top: 0; height: 60px; line-height: 60px;
    font-size: 19px; color: var(--ink);
  }
  .main-nav li.active {
    top: 7px; height: 47px; line-height: 45px; width: 106px; text-align: center;
    border: 2px solid #d8bea3; border-radius: 8px;
    background: linear-gradient(#fbeee1, #f4dcc3);
  }
  .hero-title {
    position: absolute; left: 49px; top: 103px;
    font-size: 36px; font-weight: 700; color: var(--navy); line-height: 52px;
  }
  .hero-lead {
    position: absolute; left: 49px; top: 209px; width: 640px;
    font-size: 26px; color: var(--muted); line-height: 39px;
  }
  .hero-photo {
    position: absolute; left: 702px; top: 71px; width: 349px; height: 335px;
    background: radial-gradient(ellipse at 50% 70%, #2a2a2a 0%, #3b3430 45%, rgba(240,220,200,0) 75%);
  }

  /* Content */
  .section-title {
    font-size: 26px; font-weight: 700; color: var(--navy);
  }
  .video-title { left: 61px; top: 652px; }
  .about-title { left: 394px; top: 652px; }
  .video-player {
    left: 54px; top: 702px; width: 300px; height: 230px; background: #000;
  }
  .video-player .progress {
    position: absolute; left: 0; top: 205px; width: 300px; height: 5px; background: #c4161c;
  }
  .video-player .controls {
    position: absolute; left: 0; top: 210px; width: 300px; height: 20px;
    background: linear-gradient(#2d2d2d, #151515);
  }
  .video-player .time {
    position: absolute; left: 68px; top: 3px; font-size: 9px; color: #bbb;
  }
  .about-text {
    left: 394px; top: 708px; width: 752px;
    font-family: "Noto Sans", Verdana, sans-serif;
    font-size: 13.4px; line-height: 23px; color: var(--ink);
  }
  .about-text p + p { margin-top: 23px; }

  /* Footer */
  .site-footer {
    left: 0; top: 1043px; width: 1200px; height: 145px;
    background: linear-gradient(var(--footer-bg), #f4f1ed 40%, #ebe6e0);
    border-top: 1px solid #ddd6ce;
  }
  .social-links {
    position: absolute; left: 0; top: 15px; width: 1200px; text-align: center;
    font-size: 21px; font-weight: 700; color: var(--social); word-spacing: 18px;
  }
  .footer-rule {
    position: absolute; left: 170px; top: 49px; width: 880px; height: 1px; background: var(--footer-line);
  }
  .copyright {
    position: absolute; left: 0; top: 91px; width: 1200px; text-align: center;
    font-family: "Noto Sans", Verdana, sans-serif; font-size: 16px; line-height: 26px; color: #333;
  }
</style>
</head>
<body>
  <header>
    <div class="abs top-bar">
      <div class="abs login-field username">username</div>
      <div class="abs login-field password">password</div>
      <div class="abs login-button">LOGIN</div>
    </div>
    <div class="abs brand">Ridgeloom</div>
    <div class="abs about-button"><span class="label">About Us</span><span class="icon" role="img" aria-label="Group of members icon"></span></div>
  </header>

  <section>
    <div class="abs hero-band"></div>
    <div class="abs nav-band"></div>
    <div class="abs hero-panel">
      <ul class="main-nav">
        <li class="active" style="left:20px">Home</li>
        <li style="left:143px">Bio</li>
        <li style="left:211px">Issues</li>
        <li style="left:305px">News</li>
        <li style="left:393px">Media</li>
        <li style="left:484px">Contact</li>
      </ul>
      <h1 class="hero-title">Community Site For<br>Engineers</h1>
      <p class="hero-lead">Lorem ipsum dolor sit amet, consectetuer adipiscing elit sed diam nonummy nibh euismod.</p>
      <div class="hero-photo" role="img" aria-label="Photo of two smiling engineers in business suits with arms crossed"></div>
    </div>
  </section>

  <main>
    <h2 class="abs section-title video-title">Video</h2>
    <div class="abs video-player" role="img" aria-label="Embedded video player">
      <div class="progress"></div>
      <div class="controls">
        <svg width="300" height="20" viewBox="0 0 300 20">
          <polygon points="14,5 14,15 22,10" fill="#aaa"/>
          <polygon points="46,8 49,8 53,5 53,15 49,12 46,12" fill="#aaa"/>
          <circle cx="228" cy="10" r="4" fill="#aaa"/>
          <rect x="244" y="5" width="22" height="10" rx="2" fill="#777"/>
          <rect x="277" y="5" width="10" height="10" fill="none" stroke="#aaa"/>
        </svg>
        <span class="time">0:00</span>
      </div>
    </div>

    <h2 class="abs section-title about-title">About us</h2>
    <div class="abs about-text">
      <p>Lorem ipsum dolor sit amet, consectetuer adipiscing elit, sed diam nonummy nibh euismod tincidunt ut laoreet dolore magna aliquam erat volutpat. Lorem ipsum dolor sit amet, consectetuer adipiscing elit, sed diam nonummy nibh euismod tincidunt ut laoreet dolore magna aliquam erat volutpat.</p>
      <p>Lorem ipsum dolor sit amet, consectetuer adipiscing elit, sed diam nonummy nibh euismod tincidunt ut laoreet dolore magna aliquam erat volutpat.Lorem ipsum dolor sit amet, consectetuer adipiscing elit, sed diam nonummy nibh euismod tincidunt ut laoreet dolore magna aliquam erat volutpat.Lorem ipsum dolor sit amet, consectetuer adipiscing elit, sed diam nonummy nibh euismod tincidunt ut laoreet dolore magna aliquam erat volutpat.Lorem ipsum dolor sit amet, consectetuer adipiscing elit, sed diam nonummy nibh euismod tincidunt ut laoreet dolore magna aliquam erat volutpat.</p>
    </div>
  </main>

  <footer class="abs site-footer">
    <div class="social-links">Circlebook Chirpline Orbitplus</div>
    <div class="footer-rule"></div>
    <p class="copyright">Copyright Ridgeloom.com<br>© 2012 All Rights Reserved | Privacy Policy</p>
  </footer>
</body>
</html>
```